Executive Business Card for Healthcare Company [Need Today]

I need a business card design for a healthcare company. The only branding the company has thus far is a logo. The cards will be utilized by company executives. The design I envision will be vibrant and appealing but with a corporate feel. They shouldn't be too casual or playful. I would like to complete this project TODAY if possible.

Target Market(s)

Healthcare vendors, other executives in healthcare and pharmaceuticals

Industry/Entity Type

Pharmaceutical

Contact Information for Business Card

See attachment

Font styles to use
Serif
Sans Serif

Colors

Designer to choose colors to be used in the design.

```html
<!DOCTYPE html>
<html lang="en">
<head>
<meta charset="utf-8">
<title>Corvana Therapeutics – Executive Business Card</title>
<link rel="stylesheet" href="https://fonts.googleapis.com/css2?family=Lato:wght@300;400;700&display=swap">
<style>
  :root {
    --backdrop: #ece6d3;
    --card-dark: #161616;
    --card-mid: #262626;
    --teal: #3bbdcc;
    --mint: #62d0a0;
    --text-light: #f1f1f1;
    --text-soft: #d6d6d6;
    --rule: #8a8a8a;
  }
  * { box-sizing: border-box; margin: 0; padding: 0; }
  html, body {
    width: 1200px; height: 1200px; overflow: hidden;
    background: var(--backdrop);
    font-family: "Lato", sans-serif;
  }
  .canvas { position: relative; width: 1200px; height: 1200px; }
  .card {
    position: absolute; left: 150px; width: 900px; height: 514px;
    overflow: hidden; border-radius: 4px;
    background: radial-gradient(ellipse at 65% 30%, var(--card-mid) 0%, var(--card-dark) 70%);
    box-shadow: 0 14px 30px rgba(60, 50, 30, 0.25);
  }
  .card--front { top: 56px; }
  .card--back { top: 630px; }

  /* front */
  .identity { position: absolute; left: 100px; top: 92px; }
  .identity__name { color: var(--teal); font-size: 36px; font-weight: 400; letter-spacing: 0.3px; }
  .identity__title { color: var(--text-soft); font-size: 23px; font-weight: 300; margin-top: 4px; }
  .identity__company { color: var(--text-light); font-size: 23px; font-weight: 700; margin-top: 2px; }

  .accent-ring { position: absolute; left: 0; top: 0; width: 900px; height: 514px; }

  .contact-rule {
    position: absolute; left: 560px; top: 215px; width: 1px; height: 235px;
    background: var(--rule);
  }
  .contact { position: absolute; left: 590px; top: 212px; list-style: none; }
  .contact__item {
    display: flex; align-items: center; gap: 10px;
    color: var(--text-soft); font-size: 22px; font-weight: 300; height: 30px;
  }
  .contact__item--gap { margin-top: 12px; }
  .contact__icon {
    width: 24px; height: 24px; border-radius: 50%;
    background: var(--text-light); display: flex; align-items: center; justify-content: center;
    flex: none;
  }
  .address { position: absolute; left: 610px; top: 376px; color: var(--text-light); font-size: 22px; font-weight: 400; line-height: 30px; }

  /* back */
  .brand {
    position: absolute; left: 0; top: 0; width: 100%; height: 100%;
    display: flex; align-items: center; justify-content: center; gap: 34px;
  }
  .brand__ring {
    width: 200px; height: 200px; border-radius: 50%;
    border: 5px solid var(--mint);
  }
  .brand__rule { width: 2px; height: 110px; background: var(--rule); }
  .brand__name { color: var(--teal); font-size: 60px; font-weight: 400; line-height: 1.05; letter-spacing: 0.5px; }
</style>
</head>
<body>
<main class="canvas">

  <section class="card card--front" aria-label="Business card front">
    <svg class="accent-ring" viewBox="0 0 900 514" aria-hidden="true">
      <defs>
        <linearGradient id="ringGradient" x1="0" y1="1" x2="1" y2="0">
          <stop offset="0" stop-color="#3bbdcc"/>
          <stop offset="1" stop-color="#62d0a0"/>
        </linearGradient>
      </defs>
      <circle cx="250" cy="500" r="200" fill="none" stroke="url(#ringGradient)" stroke-width="7"/>
    </svg>

    <div class="identity">
      <h1 class="identity__name">Martin Hale</h1>
      <p class="identity__title">Senior Director of Marketing</p>
      <p class="identity__company">Corvana Therapeutics, LLC</p>
    </div>

    <div class="contact-rule"></div>
    <ul class="contact">
      <li class="contact__item">
        <span class="contact__icon"><svg width="12" height="16" viewBox="0 0 12 16"><rect x="1" y="0.5" width="10" height="15" rx="2" fill="#161616"/><rect x="3" y="2.5" width="6" height="9" fill="#f1f1f1"/></svg></span>
        555-214-0387
      </li>
      <li class="contact__item">
        <span class="contact__icon"><svg width="16" height="14" viewBox="0 0 16 14"><path d="M1 5 Q8 -1 15 5 L13 7 L11 5 L5 5 L3 7 Z" fill="#161616"/><rect x="3" y="7" width="10" height="6" rx="1" fill="#161616"/></svg></span>
        555-214-0952
      </li>
      <li class="contact__item contact__item--gap">
        <span class="contact__icon"><svg width="16" height="12" viewBox="0 0 16 12"><rect x="0.5" y="0.5" width="15" height="11" rx="1" fill="#161616"/><path d="M1 1 L8 7 L15 1" stroke="#f1f1f1" stroke-width="1.4" fill="none"/></svg></span>
        mhale@corvanarx.com
      </li>
      <li class="contact__item">
        <span class="contact__icon"><svg width="16" height="16" viewBox="0 0 16 16"><circle cx="8" cy="8" r="7" fill="none" stroke="#161616" stroke-width="1.5"/><ellipse cx="8" cy="8" rx="3" ry="7" fill="none" stroke="#161616" stroke-width="1.3"/><path d="M1 8 H15" stroke="#161616" stroke-width="1.3"/></svg></span>
        www.corvanarx.com
      </li>
    </ul>
    <p class="address">118 Linden Park Avenue<br>Fairview, GA 30412</p>
  </section>

  <section class="card card--back" aria-label="Business card back">
    <div class="brand">
      <div class="brand__ring"></div>
      <div class="brand__rule"></div>
      <p class="brand__name">corvana<br>therapeutics</p>
    </div>
  </section>

</main>
</body>
</html>
```